Harbor Ridge Capital and Investments

Create a simple business card design using the logos attached. Make it similar but not exact to the reference photo. Brand guidelines are also included.

```html
<!DOCTYPE html>
<html lang="en">
<head>
<meta charset="utf-8">
<title>Harbor Ridge Capital – Business Card</title>
<link href="https://fonts.googleapis.com/css2?family=Montserrat:wght@400;500;700;800&display=swap" rel="stylesheet">
<style>
  :root {
    --navy: #0b1142;
    --navy-soft: #1a2460;
    --copper: #b2531a;
    --white: #ffffff;
    --ink: #1b2150;
    --stage: #2b2b2d;
  }
  * { box-sizing: border-box; margin: 0; padding: 0; }
  html, body {
    width: 1200px; height: 875px; overflow: hidden;
    background: var(--stage);
    font-family: "Montserrat", sans-serif;
  }
  .canvas {
    position: relative; width: 1200px; height: 875px;
  }
  .card {
    position: absolute;
    width: 525px; height: 300px;
    border-radius: 18px;
    overflow: hidden;
  }
  .card-front {
    left: 70px; top: 110px;
    background: var(--navy);
  }
  .front-pattern {
    position: absolute; inset: 0;
    background: linear-gradient(120deg, var(--navy-soft) 0%, var(--navy) 45%, var(--navy) 100%);
  }
  .front-brand {
    position: absolute; inset: 0;
    display: flex; align-items: center; justify-content: center; gap: 14px;
  }
  .brand-dot {
    width: 22px; height: 22px; border-radius: 50%;
    background: var(--copper);
  }
  .front-brand .brand-name {
    font-weight: 700; font-size: 30px; letter-spacing: 3px;
    text-transform: uppercase; color: var(--white);
  }
  .card-back {
    left: 605px; top: 465px;
    background: var(--white);
    padding: 38px 40px;
  }
  .back-brand {
    display: flex; align-items: center; gap: 10px;
    margin-bottom: 26px;
  }
  .back-brand .brand-dot { width: 14px; height: 14px; }
  .back-brand .brand-name {
    font-weight: 700; font-size: 17px; letter-spacing: 2px;
    text-transform: uppercase; color: var(--ink);
  }
  .person-name {
    font-weight: 800; font-size: 24px; color: var(--ink);
    line-height: 1.1;
  }
  .person-title {
    font-weight: 500; font-size: 13px; color: var(--ink);
    margin-top: 4px; margin-bottom: 18px;
  }
  .address {
    font-size: 12.5px; color: var(--ink); line-height: 1.35;
    margin-bottom: 16px;
  }
  .contact-list { list-style: none; }
  .contact-list li {
    display: flex; align-items: center; gap: 9px;
    font-size: 12.5px; color: var(--ink); line-height: 1.6;
  }
  .contact-icon { width: 12px; height: 12px; flex: none; }
</style>
</head>
<body>
<main class="canvas">
  <section class="card card-front">
    <div class="front-pattern" role="img" aria-label="Subtle repeating brand pattern in deep navy tones"></div>
    <div class="front-brand">
      <span class="brand-dot"></span>
      <span class="brand-name">Harbor Ridge Capital</span>
    </div>
  </section>

  <section class="card card-back">
    <div class="back-brand">
      <span class="brand-dot"></span>
      <span class="brand-name">Harbor Ridge Capital</span>
    </div>
    <h1 class="person-name">Marcus Hale</h1>
    <p class="person-title">Managing Director</p>
    <p class="address">48 Linden Ave Suite<br>310 Ashford, PA 19044</p>
    <ul class="contact-list">
      <li>
        <svg class="contact-icon" viewBox="0 0 12 12"><path d="M2 1h2.5l1 2.5-1.5 1a6 6 0 0 0 3.5 3.5l1-1.5 2.5 1V11A9 9 0 0 1 1 2z" fill="var(--copper)"/></svg>
        0419283640
      </li>
      <li>
        <svg class="contact-icon" viewBox="0 0 12 12"><rect x="0.5" y="2" width="11" height="8" rx="1" fill="var(--copper)"/><path d="M1 2.5l5 4 5-4" stroke="#fff" stroke-width="1" fill="none"/></svg>
        info@harborridgecapital.com
      </li>
      <li>
        <svg class="contact-icon" viewBox="0 0 12 12"><circle cx="6" cy="6" r="5.2" fill="none" stroke="var(--copper)" stroke-width="1.4"/><path d="M1 6h10M6 1c-2.5 3-2.5 7 0 10M6 1c2.5 3 2.5 7 0 10" stroke="var(--copper)" stroke-width="1" fill="none"/></svg>
        www.harborridgecapital.com
      </li>
    </ul>
  </section>
</main>
</body>
</html>
```